New Business Card Design Project

Target Market(s)

Passing cards out

Industry/Entity Type

Asphalt contractor

Contact Information for Business Card

Ridgefold Paving

Colors
FFC000
F8CF3A
FAE287
FDF2CF
FEFAEE
F0912C
F2A743
F7CA91
FBE8D2
FDF5EE
EE7325
F08F49
F5BC92
FAE3D3
FDF4ED

Requirements
Must have
• Asphalt
Nice to have
• Would like to have 2 pictures on it of equipment

```html
<!DOCTYPE html>
<html lang="en">
<head>
<meta charset="utf-8">
<title>Ridgefold Paving – Business Card</title>
<link href="https://fonts.googleapis.com/css2?family=Open+Sans:wght@600;700;800&display=swap" rel="stylesheet">
<style>
  :root {
    --stage: #b9b9b9;
    --orange: #ee7325;
    --yellow: #f9c013;
    --red: #e1252b;
    --ink: #2a2a2a;
    --white: #ffffff;
    --photo-sky: #a9b7c2;
    --photo-ground: #6f7166;
  }
  * { box-sizing: border-box; margin: 0; padding: 0; }
  html, body { width: 1200px; height: 815px; overflow: hidden; }
  body {
    background: var(--stage);
    font-family: "Open Sans", sans-serif;
    position: relative;
  }
  .card {
    position: absolute;
    top: 248px;
    width: 560px;
    height: 320px;
    background: var(--orange);
    overflow: hidden;
  }
  .card--front { left: 27px; }
  .card--back { left: 613px; }
  .card__frame {
    position: absolute;
    inset: 12px;
    border: 3px solid var(--ink);
    overflow: hidden;
  }
  /* Front */
  .front__shapes { position: absolute; inset: 0; }
  .front__headline {
    position: absolute;
    left: 18px; top: 11px;
    color: var(--red);
    font-weight: 800;
    font-size: 27px;
    letter-spacing: 0.5px;
    white-space: nowrap;
  }
  .services {
    position: absolute;
    left: 22px; top: 88px;
    list-style: none;
    color: var(--white);
    font-weight: 700;
    font-size: 17px;
    line-height: 24px;
  }
  .services li::before {
    content: "";
    display: inline-block;
    width: 6px; height: 6px;
    border-radius: 50%;
    background: var(--red);
    margin-right: 10px;
    vertical-align: middle;
  }
  .brand {
    position: absolute;
    right: 22px; top: 96px;
    display: flex;
    align-items: center;
    gap: 10px;
    color: var(--ink);
    font-weight: 800;
    font-size: 24px;
    white-space: nowrap;
  }
  .brand__dot {
    width: 22px; height: 22px;
    border-radius: 50%;
    background: var(--ink);
  }
  .phones {
    position: absolute;
    right: 18px; bottom: 14px;
    display: flex;
    gap: 26px;
    align-items: center;
    color: var(--red);
    font-weight: 800;
    font-size: 24px;
  }
  .phone { display: flex; align-items: center; gap: 8px; }
  .phone svg { width: 22px; height: 22px; }
  /* Back */
  .card--back .card__frame { background: var(--yellow); }
  .back__tagline {
    position: absolute;
    right: 22px; top: 10px;
    color: var(--red);
    font-weight: 800;
    font-size: 28px;
    letter-spacing: 1px;
    white-space: nowrap;
  }
  .photos {
    position: absolute;
    left: 22px; right: 22px; top: 58px;
    display: flex;
    gap: 16px;
  }
  .photo {
    flex: 1;
    height: 138px;
    border: 4px solid var(--ink);
    border-radius: 4px;
    background: linear-gradient(180deg, var(--photo-sky) 0%, #8d9a86 45%, var(--photo-ground) 100%);
  }
  .back__web {
    position: absolute;
    left: 22px; top: 206px;
    color: var(--red);
    font-weight: 800;
    font-size: 30px;
    letter-spacing: 0.5px;
    white-space: nowrap;
  }
  .people {
    position: absolute;
    left: 60px; right: 40px; top: 250px;
    display: flex;
    justify-content: space-between;
    color: var(--red);
    font-weight: 600;
    font-size: 22px;
  }
</style>
</head>
<body>
  <section class="card card--front">
    <div class="card__frame">
      <svg class="front__shapes" width="530" height="290" viewBox="0 0 530 290" aria-hidden="true">
        <rect width="530" height="290" fill="var(--orange)"/>
        <rect width="530" height="52" fill="var(--white)"/>
        <polygon points="255,226 530,226 530,290 215,290" fill="var(--yellow)"/>
      </svg>
      <h1 class="front__headline">SPECIALIST IN CHIPSEAL &amp; HOTMIX</h1>
      <ul class="services">
        <li>Ranch Roads</li>
        <li>City Streets</li>
        <li>Sub Division</li>
        <li>Patching</li>
        <li>Driveways</li>
        <li>Parking Lots</li>
      </ul>
      <div class="brand"><span class="brand__dot"></span>Ridgefold Paving</div>
      <div class="phones">
        <span class="phone">
          <svg viewBox="0 0 24 24" aria-hidden="true"><path fill="var(--red)" d="M6.6 10.8a15.1 15.1 0 0 0 6.6 6.6l2.2-2.2a1 1 0 0 1 1-.25 11.4 11.4 0 0 0 3.6.57 1 1 0 0 1 1 1V20a1 1 0 0 1-1 1A17 17 0 0 1 3 4a1 1 0 0 1 1-1h3.5a1 1 0 0 1 1 1c0 1.25.2 2.45.57 3.57a1 1 0 0 1-.25 1z"/></svg>
          555-214-7730
        </span>
        <span class="phone">
          555-386-1049
          <svg viewBox="0 0 24 24" aria-hidden="true"><path fill="var(--red)" d="M6.6 10.8a15.1 15.1 0 0 0 6.6 6.6l2.2-2.2a1 1 0 0 1 1-.25 11.4 11.4 0 0 0 3.6.57 1 1 0 0 1 1 1V20a1 1 0 0 1-1 1A17 17 0 0 1 3 4a1 1 0 0 1 1-1h3.5a1 1 0 0 1 1 1c0 1.25.2 2.45.57 3.57a1 1 0 0 1-.25 1z"/></svg>
        </span>
      </div>
    </div>
  </section>

  <section class="card card--back">
    <div class="card__frame">
      <p class="back__tagline">Doing It Right Since 1992</p>
      <div class="photos">
        <div class="photo" role="img" aria-label="Photo of a white asphalt distributor truck on a freshly sealed street"></div>
        <div class="photo" role="img" aria-label="Photo of a chrome tank sealcoat truck parked on gravel under trees"></div>
      </div>
      <p class="back__web">www.ridgefoldpaving.com</p>
      <div class="people">
        <span class="person">Dale Harlan</span>
        <span class="person">Cody Harlan</span>
      </div>
    </div>
  </section>
</body>
</html>
```